Small environmental consultancy needs a simple but professional web design

We are a boutique environmental consultancyand contracting business located in Margaret River in the South West of Western Australia.

We have two arms
1) Consulting which offers environmental planning, management and assessment services primarily to local government and the development industry.
2) Contracting which implements on site plans and on ground works primarily involving revegetation, bush regeneration and environmental weed control.

We need a simple yet professional web design within the wordpress platform that commmunicates professionalism, experience and technical expertise without appearing too corporate.

Something like this structure appeals:
http://verdantia.net.au/environment-services/
or
http://www.ridgefallenvironmental.com.au/index.php

(without the image gallery function)

Target Market(s)

Local Government Officers deciding on tenders;
Developers, Engineers, Town Planning consultants looking for environmental expertise

Industry/Entity Type

Business

Number of Pages Required

5+ page

Font styles to use
Sans Serif

Colors
33a6d7
9bcb3c

Requirements
Must have
• Pages required include:
• Home
• Environmental Planning and Management
• Revegetation and Regeneration Implementation (This page can mirror the Environmental Planning and Management page exactly in structure but with different text and images)
• About Us (I think that this page can be relatively simple and generic)
• Contact (I think that this page can be very simple and generic)
Nice to have
• An ability to start out basic and quicikly establish a website presence and then build in additional drop downs and pages over time.
Should not have
• It does not need a photo gallery page;
• It does not need a major amount of space dedicated to social media and blogs etc as this is not currently particularly active area for us

```html
<!DOCTYPE html>
<html lang="en">
<head>
<meta charset="utf-8">
<title>Company – Environmental Consultancy</title>
<link href="https://fonts.googleapis.com/css2?family=Roboto:wght@300;400;500;700&display=swap" rel="stylesheet">
<style>
:root{
  --green:#9bcb3c;
  --blue:#33a6d7;
  --ink:#222222;
  --text:#555555;
  --muted:#9a9a9a;
  --dark:#333333;
  --darker:#2b2b2b;
  --darkest:#1f1f1f;
  --light:#f2f2f2;
  --white:#ffffff;
}
*{box-sizing:border-box;margin:0;padding:0}
html,body{width:1200px;height:2166px;overflow:hidden;background:var(--white);font-family:'Roboto',Arial,sans-serif;color:var(--text)}
.page{position:relative;width:1200px;height:2166px}
.wrap{position:absolute;left:139px;width:922px}

/* header */
.site-header{position:absolute;top:0;left:0;width:1200px;height:113px;background:var(--white)}
.brand{position:absolute;left:137px;top:20px;font-size:35px;font-weight:500;color:var(--ink)}
.main-nav{position:absolute;right:140px;top:33px;display:flex;gap:0}
.main-nav a{font-size:15px;font-weight:500;color:var(--ink);text-decoration:none;padding:0 22px;border-left:1px solid #ddd}
.main-nav a:first-child{border-left:none}
.header-rule{position:absolute;top:113px;left:0;width:1200px;height:11px;background:var(--green)}
.service-tab{position:absolute;top:83px;height:41px;width:320px;border-radius:6px 6px 0 0;color:var(--white);font-size:12px;font-weight:500;text-transform:uppercase;text-align:center;line-height:14px;padding-top:7px}
.tab-planning{left:282px;background:var(--green)}
.tab-reveg{left:614px;background:var(--blue);box-shadow:inset 0 -8px 0 rgba(0,0,0,.12)}

/* hero */
.hero{position:absolute;top:124px;left:0;width:1200px;height:392px;background:radial-gradient(ellipse at 40% 20%,#4a5a3c 0%,#2b3526 45%,#151a14 100%)}
.hero-title{position:absolute;left:0;width:1200px;top:140px;text-align:center;font-size:44px;font-weight:300;line-height:56px;color:#dcdcdc;text-transform:uppercase;letter-spacing:1px}
.hero-title .hl-blue{color:var(--blue)}
.hero-title .hl-green{color:var(--green)}

/* welcome */
.welcome{position:absolute;top:516px;left:0;width:1200px;height:185px;background:var(--dark);text-align:center}
.welcome h1{margin-top:22px;font-size:40px;font-weight:500;color:var(--white)}
.welcome h1 span{color:var(--green)}
.welcome p{width:980px;margin:14px auto 0;font-size:13.5px;line-height:20px;color:#bdbdbd}
.welcome-pointer{position:absolute;top:701px;left:564px}

/* why us */
.why{position:absolute;top:701px;left:0;width:1200px;height:514px;background:var(--white)}
.section-title{font-size:40px;font-weight:400;color:var(--ink);text-transform:uppercase}
.why .section-title{position:absolute;top:68px;width:1200px;text-align:center}
.feature{position:absolute;top:152px;width:220px;text-align:center}
.feature svg{display:block;margin:0 auto}
.feature h3{margin-top:25px;font-size:19px;font-weight:400;color:var(--ink);line-height:23px;text-transform:uppercase}
.feature p{margin-top:16px;font-size:14px;line-height:20px;color:var(--muted)}

/* about + projects */
.info{position:absolute;top:1215px;left:0;width:1200px;height:629px;background:var(--light)}
.info-notch{position:absolute;top:0;left:560px}
.about{position:absolute;left:139px;top:62px;width:400px}
.about .section-title,.projects .section-title{font-size:29px}
.more-btn{position:absolute;right:0;top:8px;width:55px;height:20px;background:var(--blue);color:var(--white);font-size:11px;text-align:center;line-height:20px;border-radius:2px}
.about p{margin-top:18px;font-size:14.5px;line-height:21px;color:var(--muted)}
.about p:first-of-type{margin-top:22px}
.leaf-photo{position:absolute;left:-4px;top:346px;width:402px;height:170px;background:radial-gradient(circle at 65% 40%,#a6dc3a 0%,#5faa1e 45%,#2f7a10 100%)}
.projects{position:absolute;left:625px;top:62px;width:440px}
.project{position:absolute;left:0;width:440px;height:120px}
.project-thumb{position:absolute;left:0;top:0;width:161px;height:119px;border:4px solid var(--white);box-shadow:0 1px 3px rgba(0,0,0,.15)}
.project p{position:absolute;left:185px;top:38px;width:260px;font-size:15px;line-height:20px;color:var(--ink)}
.thumb-sky{background:linear-gradient(180deg,#3f8fe0 0%,#9cc8f0 60%,#6a5a3a 100%)}
.thumb-field{background:linear-gradient(180deg,#5b6a6a 0%,#e6d27a 45%,#7fae2c 60%,#4c7d18 100%)}
.thumb-mint{background:#b8dfb6}
.zoom-icon{position:absolute;left:57px;top:37px}

/* footer */
.site-footer{position:absolute;top:1844px;left:0;width:1200px;height:261px;background:var(--darker);color:#d8d8d8}
.footer-brand{position:absolute;left:139px;top:36px;font-size:48px;font-weight:500;color:var(--white);line-height:50px}
.footer-blurb{position:absolute;left:139px;top:92px;width:225px;font-size:11.5px;line-height:15px;color:#e6e6e6}
.footer-col{position:absolute;top:38px}
.footer-col h4{font-size:16px;font-weight:400;color:var(--white);margin-bottom:20px}
.footer-col li{list-style:none;font-size:12px;line-height:15px;margin-bottom:8px;color:#e0e0e0}
.footer-col p{font-size:12px;line-height:16px;color:#e0e0e0}
.footer-col strong{font-weight:700;color:var(--white)}
.col-nav{left:414px;width:200px}
.col-contact{left:647px;width:230px}
.col-edu{left:907px;width:200px}
.legal{position:absolute;top:2105px;left:0;width:1200px;height:61px;background:var(--darkest);color:#e0e0e0;font-size:13px;text-align:center;line-height:61px}
</style>
</head>
<body>
<div class="page">

  <header class="site-header">
    <div class="brand">Company Logo</div>
    <nav class="main-nav">
      <a href="#">HOME</a><a href="#">ABOUT US</a><a href="#">CONTACT</a>
    </nav>
  </header>
  <div class="header-rule"></div>
  <div class="service-tab tab-planning">Environmental Planning<br>and Management</div>
  <div class="service-tab tab-reveg">Revegetation and Regeneration<br>Implementation</div>

  <section class="hero" role="img" aria-label="Photograph of a misty forested valley with sunlit trees">
    <h2 class="hero-title"><span class="hl-blue">Positive</span> outcomes for people,<br>projects, and the <span class="hl-green">environment</span></h2>
  </section>

  <section class="welcome">
    <h1>WELCOME TO <span>COMPANY</span></h1>
    <p>We are a specialist botanical consultancy with more than 15 years of experience providing professional services that our clients trust and rely on. Our committed employees located throughout Western Australia, bring inter-disciplinary expertise to every project we work on. Our clients look to us to provide a wide range of scientific, technical and management expertise that merge to provide practical environmental solutions.</p>
  </section>
  <svg class="welcome-pointer" width="72" height="34" viewBox="0 0 72 34" aria-hidden="true"><polygon points="0,0 72,0 36,34" fill="#333333"/></svg>

  <section class="why">
    <h2 class="section-title">Why us?</h2>

    <div class="feature" style="left:124px">
      <svg width="112" height="112" viewBox="0 0 112 112" aria-hidden="true">
        <circle cx="56" cy="56" r="53" fill="none" stroke="#9bcb3c" stroke-width="5"/>
        <circle cx="56" cy="56" r="41" fill="#9bcb3c"/>
        <path d="M56 33c-9 0-16 7-16 16 0 11 16 25 16 25s16-14 16-25c0-9-7-16-16-16z" fill="#fff"/>
        <circle cx="56" cy="49" r="6" fill="#9bcb3c"/>
        <ellipse cx="56" cy="77" rx="14" ry="4" fill="none" stroke="#fff" stroke-width="2.5"/>
      </svg>
      <h3>Location</h3>
      <p>Lorem ipsum dolor sit amet, consectetur adipiscing elit, sed do eiusmod tempor incididunt ut labore et dolore magna aliqua.</p>
    </div>

    <div class="feature" style="left:365px">
      <svg width="112" height="112" viewBox="0 0 112 112" aria-hidden="true">
        <circle cx="56" cy="56" r="53" fill="none" stroke="#9bcb3c" stroke-width="5"/>
        <circle cx="56" cy="56" r="41" fill="#9bcb3c"/>
        <circle cx="48" cy="44" r="8" fill="#fff"/>
        <path d="M33 72c0-10 7-16 15-16s15 6 15 16z" fill="#fff"/>
        <circle cx="66" cy="48" r="7" fill="#fff"/>
        <path d="M60 72c0-5 0-9-3-12 2-2 5-3 9-3 8 0 13 6 13 15z" fill="#fff"/>
      </svg>
      <h3>Staff diversity<br>&amp; training</h3>
      <p>Sed ut perspiciatis unde omnis iste natus error sit voluptatem accusantium doloremque laudantium, totam rem aperiam.</p>
    </div>

    <div class="feature" style="left:606px">
      <svg width="112" height="112" viewBox="0 0 112 112" aria-hidden="true">
        <circle cx="56" cy="56" r="53" fill="none" stroke="#9bcb3c" stroke-width="5"/>
        <circle cx="56" cy="56" r="41" fill="#9bcb3c"/>
        <g stroke="#fff" stroke-width="2.5">
          <line x1="56" y1="56" x2="56" y2="35"/><line x1="56" y1="56" x2="76" y2="48"/>
          <line x1="56" y1="56" x2="72" y2="73"/><line x1="56" y1="56" x2="40" y2="73"/>
          <line x1="56" y1="56" x2="36" y2="48"/>
        </g>
        <g fill="#fff">
          <circle cx="56" cy="56" r="7"/><circle cx="56" cy="34" r="5"/><circle cx="77" cy="48" r="5"/>
          <circle cx="73" cy="74" r="5"/><circle cx="39" cy="74" r="5"/><circle cx="35" cy="48" r="5"/>
        </g>
      </svg>
      <h3>Networks and<br>relationships</h3>
      <p>I must explain to you how all this mistaken idea of denouncing pleasure and praising pain was born and I will give you a complete.</p>
    </div>

    <div class="feature" style="left:845px">
      <svg width="112" height="112" viewBox="0 0 112 112" aria-hidden="true">
        <circle cx="56" cy="56" r="53" fill="none" stroke="#9bcb3c" stroke-width="5"/>
        <circle cx="56" cy="56" r="41" fill="#9bcb3c"/>
        <rect x="40" y="32" width="32" height="46" rx="2" fill="#fff"/>
        <g fill="#9bcb3c">
          <rect x="45" y="40" width="4" height="4"/><rect x="52" y="41" width="15" height="2"/>
          <rect x="45" y="49" width="4" height="4"/><rect x="52" y="50" width="15" height="2"/>
          <rect x="45" y="58" width="4" height="4"/><rect x="52" y="59" width="15" height="2"/>
          <rect x="45" y="67" width="4" height="4"/><rect x="52" y="68" width="15" height="2"/>
        </g>
      </svg>
      <h3>Professional<br>and accountable</h3>
      <p>At vero eos et accusamus et iusto odio dignissimos ducimus qui blanditiis praesentium voluptatum deleniti atque corrupti quos dolores.</p>
    </div>
  </section>

  <section class="info">
    <svg class="info-notch" width="80" height="38" viewBox="0 0 80 38" aria-hidden="true"><polygon points="0,0 80,0 40,38" fill="#ffffff"/></svg>

    <div class="about">
      <h2 class="section-title">About</h2>
      <span class="more-btn">More +</span>
      <p>We are accountable for delivering quality, timely, sustainable, discreet, affordable environment services in a professional manner. We are also accountable to the relevant Environmental Legislation and policy including Parliamentary Acts, State and local laws.</p>
      <p>Take the time to explore our website and if the service you require isn't highlighted here don't hesitate to contact us with a brief of the project you have in mind. We have great staff diversity and would be happy to give your project due consideration.</p>
      <p>All photos displayed have been taken by staff on site during property visits.</p>
      <div class="leaf-photo" role="img" aria-label="Close-up photograph of fresh green leaves in sunlight"></div>
    </div>

    <div class="projects">
      <h2 class="section-title">Recent projects</h2>
      <div class="project" style="top:73px">
        <div class="project-thumb thumb-sky" role="img" aria-label="Photograph of hands holding soil with a young seedling against blue sky"></div>
        <p>Vestibulum sit amet mi tristique, interdum ligula id, pulvinar est.</p>
      </div>
      <div class="project" style="top:220px">
        <div class="project-thumb thumb-field" role="img" aria-label="Photograph of a green meadow at sunset"></div>
        <p>Nulla vitae ligula euismod, blandit ante sagittis, consectetur magna.</p>
      </div>
      <div class="project" style="top:368px">
        <div class="project-thumb thumb-mint" role="img" aria-label="Project photograph with zoom overlay">
          <svg class="zoom-icon" width="40" height="40" viewBox="0 0 40 40" aria-hidden="true">
            <circle cx="20" cy="20" r="20" fill="#3a3a3a"/>
            <circle cx="18" cy="18" r="7" fill="none" stroke="#fff" stroke-width="2.5"/>
            <line x1="23" y1="23" x2="29" y2="29" stroke="#fff" stroke-width="3" stroke-linecap="round"/>
          </svg>
        </div>
        <p>Maecenas eu orci ultricies neque congue mollis sit amet eu turpis.</p>
      </div>
    </div>
  </section>

  <footer class="site-footer">
    <div class="footer-brand">LOGO</div>
    <p class="footer-blurb">Lorem ipsum dolor sit amet, consec tuer adipiscing elit, sed diam nonum nibh euismod. Lotuer adipiscing elit, sed diam nibh eu.</p>
    <div class="footer-col col-nav">
      <h4>Navigation</h4>
      <ul>
        <li>Home</li>
        <li>Environmental Planning<br>and Management</li>
        <li>Revegetation and<br>Regeneration Implementation</li>
        <li>About Us</li>
        <li>Contact</li>
      </ul>
    </div>
    <div class="footer-col col-contact">
      <h4>About Us</h4>
      <p><strong>Eco</strong>, 18 Marlow Ridge Road</p>
      <p style="margin-top:34px"><strong>Phone:</strong> (+61) 8 9750 4412</p>
      <p><strong>Email:</strong> info@verdantiaeco.net</p>
    </div>
    <div class="footer-col col-edu">
      <h4>Education</h4>
      <ul>
        <li>Marine Activities</li>
        <li>River/Estuary</li>
        <li>Bush Activities</li>
        <li>AusVELS, VET/VCAL and VCE</li>
        <li>School holiday programs</li>
        <li>Cape Reed Lighthouse Tour</li>
      </ul>
    </div>
  </footer>
  <div class="legal">Copyright 2013-2015 Logo Co., Ltd., All Rights Reserved</div>

</div>
</body>
</html>
```